Spa Resort Website

UPDATE:
Note that for the home page we are intending to have a slideshow showcasing elements of the resort, as per:
* www.brackenwellpools.co.nz
* www.velanira.com
* www.wanderlofty-journeys.com
We also need to know how you intend to use the colours to denote subsections, as per the brief below.
Also...the sliders denoting Elegant vs Bold etc seem to have lost their settings. I have reset them to how I believe we set them a couple of weeks ago, but there may be minor differences.
=============================================
We are developing a website for Taupo Kelmarsh, a resort in Taupo, New Zealand.
While we have been provided with a site layout and basic colour scheme, the implementation of this design does not meet the client's needs for a modern, inviting looking site.
We require a designer to work within the outline structure of the site and provide design elements to lift the design. We envisage that these design elements would include styling of the menus, building of the colour schemes from the base colours, home page design.
If you are unsure of the parameters please post a question indicating elements you would like to change and we can comment on feasibility.
We have attached the original design concept and some of the wire framing that we developed from that.
The site has four major sections, each requiring its own, subtly different, colour scheme - these schemes are to be based on the colours in the client's logo (attached). Obviously there does need to be consistency in the colour schemes across the site. The colours from the logo apply as follows:
* Stay (accommodation) - "Orange"
* Soak (Hot Springs and water park) - "Green"
* Soothe (Spa Resort) - "Beige"
* Savour (Summary of experience) - "Choc Brown"
We require the design for 2 pages:
* Home
* Detail Page (eg Family Accommodation)
Design must be flexible in that if we decide at a later date to add another block to the RH area (for example) we are able to while maintaining the integrity of the design.
Menu items include dropdowns.
We are not happy with the current layout of the HOME page and require a full redesign of this.
The resort is 5 star, but also offers camping facilities. The design therefore needs to reflect the high quality of the resort, while also being accessible to those on a budget.
The following sites can be considered reference sites for the look and feel we are seeking:
* www.brackenwellpools.co.nz
* www.velanira.com
Final deliverable is preferred in layered PNG, but .eps is acceptable. .ai is not acceptable.

```html
<!DOCTYPE html>
<html lang="en">
<head>
<meta charset="utf-8">
<title>Taupo Kelmarsh Spa Resort – Soak</title>
<link rel="stylesheet" href="https://fonts.googleapis.com/css2?family=Questrial&family=Carlito:wght@400;700&display=swap">
<style>
  :root {
    --stay: #d45d2c;
    --soak: #0d9358;
    --soothe: #d2c19a;
    --savour: #5c3d14;
    --sage: #8fbcaa;
    --text: #3f3f3f;
    --ink: #2b2b2b;
    --link: #138a54;
    --link-visited: #4bb08a;
    --rule: #cfe3da;
    --white: #ffffff;
  }
  * { box-sizing: border-box; margin: 0; padding: 0; }
  html, body { width: 945px; height: 1200px; overflow: hidden; background: var(--white); }
  body { position: relative; font-family: "Carlito", "Calibri", sans-serif; color: var(--text); }

  .brand { position: absolute; left: 133px; top: 72px; font-family: "Questrial", sans-serif; font-size: 24px; color: var(--ink); white-space: nowrap; line-height: 1; }

  .section-tabs { position: absolute; top: 96px; left: 405px; display: flex; gap: 5px; }
  .section-tab { width: 103px; height: 28px; border-radius: 4px 4px 0 0; color: var(--white); font-family: "Questrial", sans-serif; font-size: 18px; text-align: center; line-height: 29px; border: 2px solid rgba(255,255,255,.35); border-bottom: none; }
  .tab-stay { background: var(--stay); }
  .tab-soak { background: var(--soak); }
  .tab-soothe { background: var(--soothe); }
  .tab-savour { background: var(--savour); }

  .masthead { position: absolute; left: 0; top: 124px; width: 945px; height: 249px; background: var(--soak); }
  .main-nav { position: absolute; top: 6px; left: 116px; width: 716px; height: 26px; }
  .main-nav a { position: absolute; transform: translateX(-50%); color: var(--white); text-decoration: none; font-size: 13px; top: 0; white-space: nowrap; }
  .hero { position: absolute; left: 116px; top: 32px; width: 716px; height: 215px; background: linear-gradient(180deg, #6f7c5e 0%, #8d977a 35%, #3dbfb0 60%, #36b3a3 100%); box-shadow: 0 2px 6px rgba(0,0,0,.35); }
  .band-shadow { position: absolute; left: 0; top: 373px; width: 945px; height: 24px; background: linear-gradient(#d9d9d9, #ffffff); }

  .content { position: absolute; left: 116px; top: 400px; width: 440px; font-size: 10px; line-height: 14px; }
  .content h1 { font-family: "Questrial", sans-serif; font-weight: 400; font-size: 20px; line-height: 26px; color: var(--soak); margin-bottom: 6px; }
  .content h2 { font-family: "Questrial", sans-serif; font-weight: 400; font-size: 16px; line-height: 22px; color: var(--soak); margin: 22px 0 7px; }
  .content p { margin-bottom: 14px; }
  .content a { color: var(--link); text-decoration: none; }
  .content a.visited { color: var(--link-visited); }
  .feature-list { list-style: none; margin-bottom: 12px; }
  .feature-list li { line-height: 19px; }
  .feature-list li::before { content: ">> "; color: var(--soak); }

  .column-rule { position: absolute; left: 575px; top: 413px; width: 1px; height: 560px; background: var(--rule); }

  .sidebar { position: absolute; left: 599px; top: 413px; width: 233px; }
  .cta { display: block; height: 50px; color: var(--white); text-decoration: none; font-family: "Questrial", sans-serif; font-size: 15px; text-align: center; line-height: 50px; }
  .cta-book { background: var(--soak); margin-bottom: 29px; }
  .cta-deals { background: var(--stay); height: 46px; line-height: 46px; }
  .block-title { font-family: "Questrial", sans-serif; font-weight: 400; font-size: 13px; color: #8b9a93; margin: 31px 0 4px; letter-spacing: .3px; }
  .comments { background: var(--soothe); height: 123px; padding: 10px 10px 0 10px; position: relative; }
  .comments blockquote { font-family: "Questrial", sans-serif; font-size: 11px; line-height: 18px; color: #3a3a3a; padding: 0 16px 0 18px; position: relative; }
  .quote-mark { position: absolute; font-family: Georgia, serif; font-size: 30px; color: var(--soak); font-weight: 700; line-height: 1; }
  .quote-open { left: -2px; top: 0; }
  .quote-close { right: -2px; bottom: -14px; }
  .comments a { position: absolute; right: 14px; bottom: 12px; font-size: 10px; color: var(--soak); text-decoration: none; font-family: "Questrial", sans-serif; }
  .keep-in-touch { background: var(--sage); height: 208px; padding: 18px 21px; font-family: "Questrial", sans-serif; font-size: 11px; color: #2f3a35; position: relative; }
  .keep-in-touch p { line-height: 14px; width: 170px; }
  .field { display: flex; align-items: center; margin-top: 9px; }
  .field:first-of-type { margin-top: 14px; }
  .field label { width: 46px; }
  .field span { display: block; width: 147px; height: 17px; background: var(--white); }
  .submit { position: absolute; right: 21px; top: 125px; width: 77px; height: 19px; background: var(--stay); color: var(--white); font-size: 11px; text-align: center; line-height: 19px; border-radius: 3px; }
  .follow { position: absolute; left: 21px; top: 164px; display: flex; align-items: center; gap: 9px; }
  .follow span.label { margin-right: 12px; }
  .social { width: 33px; height: 33px; border-radius: 7px; display: block; }
  .social-feed { background: #e8812c; }
  .social-chirp { background: #3aa3d9; }
  .social-friends { background: #3d62a8; }

  .site-footer { position: absolute; left: 0; top: 1031px; width: 945px; height: 169px; background: var(--sage); }
  .footer-col { position: absolute; top: 22px; font-size: 10px; line-height: 14px; color: #2f3a35; }
  .footer-col h3 { font-family: "Questrial", sans-serif; font-weight: 400; font-size: 12.5px; color: #2a2a2a; width: 106px; border-bottom: 1px solid #2a2a2a; padding-bottom: 1px; margin-bottom: 4px; }
  .footer-col ul { list-style: none; }
</style>
</head>
<body>
  <header>
    <div class="brand">Taupo Kelmarsh</div>
    <nav class="section-tabs">
      <div class="section-tab tab-stay">STAY</div>
      <div class="section-tab tab-soak">SOAK</div>
      <div class="section-tab tab-soothe">SOOTHE</div>
      <div class="section-tab tab-savour">SAVOUR</div>
    </nav>
  </header>

  <div class="masthead">
    <nav class="main-nav">
      <a href="#" style="left:59px">Home</a>
      <a href="#" style="left:191px">Accommodation</a>
      <a href="#" style="left:320px">Deals</a>
      <a href="#" style="left:417px">Prices</a>
      <a href="#" style="left:523px">Gallery</a>
      <a href="#" style="left:641px">Contact Us</a>
    </nav>
    <div class="hero" role="img" aria-label="Photo of guests relaxing in a turquoise hot spring pool surrounded by rocks, a waterfall and tropical plants"></div>
  </div>
  <div class="band-shadow"></div>

  <main class="content">
    <h1>Soak your cares away at Kelmarsh Hot Springs</h1>
    <p>Lorem ipsum onsectetuer adipiscing elit, sed diam nonummy nibh euismod tincidunt ut laoreet dolore magna aliquam erat volutpat. Ut wisi enim ad minim veniam, quis nostrud exerci tation ullamcorper suscipit lobortis nisl ut aliquip ex ea commodo consequat.</p>
    <p>Lorem ipsum onsectetuer adipiscing elit, sed diam nonummy nibh euismod tincidunt ut laoreet dolore magna aliquam erat volutpat. Ut wisi enim ad minim veniam, quis nostrud exerci tation ullamcorper suscipit lobortis nisl ut aliquip ex ea commodo consequat.</p>
    <h2>Subheading</h2>
    <p>Lorem ipsum onsectetuer adipiscing elit, sed diam nonummy nibh euismod tincidunt ut laoreet dolore magna aliquam erat volutpat. Ut wisi enim ad minim veniam, quis nostrud exerci tation ullamcorper suscipit lobortis nisl ut aliquip ex ea commodo consequat.</p>
    <p>Ut wisi enim ad minim veniam, quis nostrud exerci tation ullamcorper suscipit lobortis nisl ut aliquip ex ea commodo consequat. <a href="#">Unvisited link</a>.</p>
    <h2>Subheading</h2>
    <p>Lorem ipsum onsectetuer adipiscing elit, sed diam nonummy nibh euismod tincidunt ut laoreet dolore magna aliquam erat volutpat. Ut wisi enim ad minim veniam, quis nostrud exerci tation ullamcorper suscipit lobortis nisl ut aliquip ex ea commodo consequat.</p>
    <p>Ut wisi enim ad minim veniam, quis nostrud exerci tation ullamcorper suscipit lobortis nisl ut aliquip ex ea commodo consequat. <a href="#" class="visited">Visited link</a>.</p>
    <h2>Subheading</h2>
    <p>Lorem ipsum onsectetuer adipiscing elit, sed diam nonummy nibh euismod tincidunt ut laoreet dolore magna aliquam erat volutpat.</p>
    <ul class="feature-list">
      <li>Ut wisi enim ad minim veniam</li>
      <li>Quis nostrud exerci tation ullamcorper</li>
      <li>Suscipit lobortis nisl ut aliquip ex ea commodo consequat</li>
    </ul>
    <p>Ut wisi enim ad minim veniam, quis nostrud exerci tation ullamcorper suscipit lobortis nisl ut aliquip ex ea commodo consequat.</p>
  </main>

  <div class="column-rule"></div>

  <aside class="sidebar">
    <a href="#" class="cta cta-book">BOOK AND PAY ONLINE</a>
    <a href="#" class="cta cta-deals">GREAT DEALS AND SPECIALS</a>

    <h3 class="block-title">CUSTOMER COMMENTS</h3>
    <div class="comments">
      <blockquote>
        <span class="quote-mark quote-open">&ldquo;</span>
        Lorem ipsum onsectetuer adipi-scing elit, sed diam nonummy nibh euismod tincidunt ut laoreet dolore magna aliquam erat volutpat!
        <span class="quote-mark quote-close">&rdquo;</span>
      </blockquote>
      <a href="#">Read more comments</a>
    </div>

    <h3 class="block-title">KEEP IN TOUCH</h3>
    <div class="keep-in-touch">
      <p>Keep up to date with what's happening in Taupo and at Kelmarsh!</p>
      <div class="field"><label>Name:</label><span></span></div>
      <div class="field"><label>Email:</label><span></span></div>
      <div class="submit">Submit!</div>
      <div class="follow">
        <span class="label">Follow us:</span>
        <span class="social social-feed" role="img" aria-label="News feed"></span>
        <span class="social social-chirp" role="img" aria-label="Short updates"></span>
        <span class="social social-friends" role="img" aria-label="Social page"></span>
      </div>
    </div>
  </aside>

  <footer class="site-footer">
    <div class="footer-col" style="left:116px">
      <h3>STAY</h3>
      <ul><li>Spa Resort</li><li>Spa Chalets</li><li>Accommodation</li><li>Motels</li><li>Cabins</li><li>Camping</li></ul>
    </div>
    <div class="footer-col" style="left:295px">
      <h3>SOAK</h3>
      <ul><li>Mineral Bathing</li><li>Outdoor Pools</li><li>Water Playground</li></ul>
    </div>
    <div class="footer-col" style="left:468px">
      <h3>SOOTHE</h3>
      <ul><li>Spa Resort</li><li>Spa Chalets</li><li>Accommodation</li><li>Motels</li><li>Cabins</li><li>Camping</li></ul>
    </div>
    <div class="footer-col" style="left:652px">
      <h3>SAVOUR</h3>
      <ul><li>Spa Resort</li><li>Spa Chalets</li><li>Accommodation</li><li>Motels</li><li>Cabins</li><li>Camping</li></ul>
    </div>
  </footer>
</body>
</html>
```